Tovin Marsk Technologies Web Site

I need website designed for Tovin Marsk Technologies, LLC. It is an email marketing software as a service business. I am looking for a five page website with the ability to accept payments. I have included our logo below for integration with the website. I do not have the text ready yet.

The domain to use is tovin-marsk.com

I have also included some examples of other websites that outline the basic structure I would like
https://trybluvesto.com/
https://www.postvaro.com/

I know I need to provide some more information, but I want to get the ball rolling and see what is needed.
Thanks!
Eli

```html
<!DOCTYPE html>
<html lang="en">
<head>
<meta charset="utf-8">
<title>Customers – Tovin Marsk Technologies</title>
<link rel="stylesheet" href="https://fonts.googleapis.com/css2?family=Arimo:wght@400;700&family=Cinzel:wght@600;700&family=Oswald:wght@600&display=swap">
<style>
:root{
  --navy:#27215f;
  --navy-deep:#1f1b5c;
  --red:#ee1c25;
  --sky:#4a9ee8;
  --panel:#fafafa;
  --card:#ececec;
  --text:#555;
  --rule:#c9c9c9;
  --client:#b3b3b3;
}
*{margin:0;padding:0;box-sizing:border-box}
html,body{width:686px;height:1200px;overflow:hidden}
body{position:relative;background:var(--navy);font-family:"Arimo",Arial,sans-serif;color:var(--text)}
.backdrop{position:absolute;left:0;top:0}
.brand{position:absolute;left:0;width:686px;text-align:center}
.brand-mark{display:block;margin:0 auto;border-radius:50%;border:2px solid var(--sky)}
.brand-name{display:block;font-family:"Arimo",Arial,sans-serif;font-weight:400;color:var(--sky);letter-spacing:1px}
.main-nav{position:absolute;left:0;top:106px;width:686px;height:21px;border-top:1px solid #3d3780;border-bottom:1px solid #3d3780;display:flex;justify-content:center;align-items:center;gap:22px}
.main-nav a{font-family:"Cinzel",serif;font-weight:600;font-size:8px;color:var(--sky);text-decoration:none;letter-spacing:.3px}
.main-nav a.current{color:#fff}
.panel{position:absolute;left:20px;top:134px;width:628px;height:892px;background:var(--panel)}
.hero{position:absolute;left:29px;top:24px;width:587px;height:118px;background:linear-gradient(100deg,#3a3f8a 0%,#4b5a9e 45%,#3d4590 100%);border:1px solid #2c2a6e}
.hero-title{position:absolute;left:0;top:24px;width:100%;text-align:center;font-family:"Cinzel",serif;font-weight:700;font-size:13px;color:#fff;letter-spacing:.5px}
.hero-title::before,.hero-title::after{content:"";position:absolute;top:9px;width:135px;height:1px;background:rgba(255,255,255,.45)}
.hero-title::before{left:87px}.hero-title::after{right:113px}
.hero-lead{position:absolute;left:0;top:50px;width:100%;text-align:center;font-size:9.6px;color:#fff}
.hero-contacts{position:absolute;left:0;top:80px;width:100%;display:flex;justify-content:center;align-items:center;font-size:7.5px;color:#6fc0ff;font-weight:700}
.hero-contacts span{display:flex;align-items:center;gap:6px}
.hero-contacts .divider{width:1px;height:20px;background:rgba(255,255,255,.4);margin:0 22px}
.section-title{position:absolute;font-weight:700;font-size:10.5px;color:var(--navy-deep)}
.copy{position:absolute;left:55px;width:500px;font-size:8.3px;line-height:10.5px}
.review{position:absolute;top:316px;width:162px;height:259px;background:var(--card)}
.review-photo{position:absolute;left:24px;top:22px;width:110px;height:109px;background:linear-gradient(160deg,#c9d3dc 0%,#8a98aa 45%,#28344d 100%)}
.review-name{position:absolute;left:24px;top:142px;font-size:9.5px;font-weight:400;color:var(--navy-deep)}
.review-text{position:absolute;left:24px;top:160px;width:122px;font-size:7.3px;line-height:9.4px;color:#666}
.clients-title{position:absolute;left:0;top:636px;width:100%;text-align:center;font-weight:700;font-size:9.6px;color:var(--navy-deep)}
.clients-rule{position:absolute;top:642px;height:1px;background:var(--rule)}
.client{position:absolute;top:676px;display:flex;align-items:center;gap:5px;font-weight:700;color:var(--client);white-space:nowrap}
.client .dot{width:20px;height:20px;border-radius:50%;background:var(--client)}
.illustration{position:absolute;left:84px;top:750px;width:484px;height:142px;background:linear-gradient(180deg,#f6f6f9 0%,#e8e9f1 60%,#eef0f6 100%)}
.footer-title{position:absolute;left:66px;top:1054px;font-family:"Oswald",sans-serif;font-weight:600;font-size:14.5px;color:#fff}
.footer-text{position:absolute;font-size:7.6px;line-height:13px;color:#fff}
.footer-note{position:absolute;left:450px;width:180px;font-size:7.4px;line-height:9.6px;color:#c9cbe6}
.subscribe{position:absolute;left:450px;top:1112px;width:68px;height:18px;border:1px solid var(--sky);border-radius:3px;color:var(--sky);font-size:8.5px;text-align:center;line-height:16px}
.footer-rule{position:absolute;left:66px;top:1155px;width:558px;height:1px;background:#4a4590}
.social{position:absolute;top:1166px;width:21px;height:21px;border:1.5px solid #fff;border-radius:50%}
</style>
</head>
<body>
<svg class="backdrop" width="686" height="1200" aria-hidden="true">
  <polygon points="0,344 686,156 686,996 0,996" fill="var(--red)"/>
</svg>

<div class="brand" style="top:10px">
  <span class="brand-mark" style="width:56px;height:56px"></span>
  <span class="brand-name" style="font-size:14px;margin-top:9px">TOVIN MARSK</span>
</div>

<nav class="main-nav">
  <a href="#">Home</a><a href="#">Solution</a><a href="#">Pricing</a><a href="#" class="current">Customers</a><a href="#">ContactUs</a>
</nav>

<main class="panel">
  <section class="hero" role="img" aria-label="Photo of people working at a desk with documents">
    <h1 class="hero-title">Customers</h1>
    <p class="hero-lead">Lorem ipsum dolor sit amet, consectetur adipiscing elit. Ut purus ex,</p>
    <div class="hero-contacts">
      <span>
        <svg width="14" height="14" viewBox="0 0 24 24" aria-hidden="true"><path fill="#fff" d="M6.6 10.8a15 15 0 0 0 6.6 6.6l2.2-2.2c.3-.3.7-.4 1-.2 1.1.4 2.3.6 3.6.6.6 0 1 .4 1 1V20c0 .6-.4 1-1 1A17 17 0 0 1 3 4c0-.6.4-1 1-1h3.5c.6 0 1 .4 1 1 0 1.3.2 2.5.6 3.6.1.3 0 .7-.2 1z"/></svg>
        (309) 555-0142
      </span>
      <i class="divider"></i>
      <span>
        <svg width="14" height="12" viewBox="0 0 24 20" aria-hidden="true"><rect x="1" y="3" width="22" height="16" fill="#fff"/><path d="M1 3l11 9 11-9" fill="none" stroke="#4b5a9e" stroke-width="1.5"/></svg>
        Email Us
      </span>
    </div>
  </section>

  <h2 class="section-title" style="left:54px;top:168px">Our Happy Customers</h2>
  <p class="copy" style="top:189px">Staying close to our customers is second nature to us. We pride ourselves on understanding that businesses come in all shapes and sizes, from start-ups to small and medium sized businesses, and mid-market companies.</p>
  <p class="copy" style="top:221px">Our customers range from business owners to bookkeepers and finance directors, all of whom have different requirements. While every one is unique they all share common challenges and goals - a desire for simple, secure and smart solutions that reduce complexity and risk. And when they have problems that need resolving, they want to speak to a real person – someone they can trust. So we make sure we’re always there to listen and help.</p>

  <h2 class="section-title" style="left:55px;top:293px">Customer Reviews</h2>

  <article class="review" style="left:55px">
    <div class="review-photo" role="img" aria-label="Portrait photo of a customer in a suit"></div>
    <h3 class="review-name">Name</h3>
    <p class="review-text">Create list and list groups to better categorize the list of one sort, per-form number of quick actions to manage the list and the contacts within.</p>
  </article>
  <article class="review" style="left:228px">
    <div class="review-photo" role="img" aria-label="Portrait photo of a customer in a suit"></div>
    <h3 class="review-name">Name</h3>
    <p class="review-text">Get rid of storing contacts data in limited number of fields, use custom field function to store additional contact info. Setup as many as you find necessary.</p>
  </article>
  <article class="review" style="left:401px">
    <div class="review-photo" role="img" aria-label="Portrait photo of a customer in a suit"></div>
    <h3 class="review-name">Name</h3>
    <p class="review-text">Control how and who do you want to communicate, setup “Don’t Send to List” and auto-matically omit unwanted emails, domains and IPs while sending your campaigns.</p>
  </article>

  <div class="clients-rule" style="left:22px;width:202px"></div>
  <h2 class="clients-title">Previous Clients</h2>
  <div class="clients-rule" style="left:391px;width:212px"></div>

  <div class="client" style="left:54px;font-size:9.5px"><i class="dot"></i>Brightlane</div>
  <div class="client" style="left:174px;font-size:9.5px">Northfield Institute</div>
  <div class="client" style="left:300px;font-size:16px">Corvana</div>
  <div class="client" style="left:433px;font-size:20px">Velto</div>
  <div class="client" style="left:530px;font-size:14px">quillet</div>

  <div class="illustration" role="img" aria-label="Line illustration of a person opening an email surrounded by marketing icons"></div>
</main>

<h2 class="footer-title">Contact</h2>
<p class="footer-text" style="left:66px;top:1077px;font-weight:700;font-size:8.8px">Tovin Marsk Technologies</p>
<p class="footer-text" style="left:66px;top:1091px">2290 W. Larchmont Ct.<br>Ashford, IL 60420<br>Phone: (309) 555-0142</p>

<div class="brand" style="top:1058px;left:273px;width:200px">
  <span class="brand-mark" style="width:44px;height:44px"></span>
  <span class="brand-name" style="font-size:11px;margin-top:8px">TOVIN MARSK</span>
</div>

<p class="footer-note" style="top:1061px">We will soon be launching our new email market-ing software as a service (Saas).</p>
<p class="footer-note" style="top:1090px">Please stay tuned for important updates.</p>
<a class="subscribe">Subscribe</a>

<div class="footer-rule"></div>
<span class="social" style="left:280px"></span>
<span class="social" style="left:311px"></span>
<span class="social" style="left:341px"></span>
<span class="social" style="left:372px"></span>
</body>
</html>
```